Chimney Service company needs new business card design

We need a updated business card with our new logo added. We provide a full range of chimney services throughout Vermont and New Hampshire. The business card will be one sided and color. Attached is our current business card another document showing all the information we would like on the card.
We dont like a lot of flashy colors.... here is a link to our website to get an idea of our branding www.flueguardianvt.example

Target Market(s)

homeowners

Industry/Entity Type

Business

Contact Information for Business Card

See attached sheet for content.

Font styles to use
Serif
Sans Serif

Requirements
Must have
• all information provided on separate sheet
Should not have
• Additional information that may clogg up design

```html
<!DOCTYPE html>
<html lang="en">
<head>
<meta charset="utf-8">
<title>Flue Guardian Business Card</title>
<link href="https://fonts.googleapis.com/css2?family=Cinzel:wght@500&family=Bebas+Neue&family=Roboto:wght@400&display=swap" rel="stylesheet">
<style>
  :root {
    --backdrop: #2a2a2a;
    --card: #f7f7f5;
    --charcoal: #333333;
    --ink: #444444;
    --brand-red: #9b1116;
  }
  html, body {
    margin: 0;
    width: 1200px;
    height: 871px;
    overflow: hidden;
    background: var(--backdrop);
  }
  .business-card {
    position: absolute;
    left: 100px;
    top: 150px;
    width: 1000px;
    height: 572px;
    background: var(--card);
  }
  .brand-block {
    position: absolute;
    left: 23px;
    top: 34px;
    width: 515px;
    height: 508px;
    display: flex;
    align-items: center;
    justify-content: center;
    gap: 18px;
  }
  .brand-block-square {
    width: 34px;
    height: 34px;
    background: var(--brand-red);
    flex: none;
  }
  .brand-block-name {
    font-family: "Cinzel", serif;
    font-weight: 500;
    font-size: 44px;
    letter-spacing: 1px;
    color: var(--charcoal);
    line-height: 1;
  }
  .details {
    position: absolute;
    left: 573px;
    top: 62px;
    width: 410px;
    color: var(--ink);
  }
  .company-name {
    margin: 0;
    font-family: "Cinzel", serif;
    font-weight: 500;
    font-size: 40px;
    letter-spacing: 1px;
    color: var(--charcoal);
    line-height: 1;
  }
  .established {
    margin: 6px 0 0;
    width: 372px;
    text-align: center;
    font-family: "Cinzel", serif;
    font-size: 15px;
    letter-spacing: 2px;
    color: var(--charcoal);
  }
  .credentials {
    margin: 34px 0 0;
    font-family: "Bebas Neue", sans-serif;
    font-size: 29px;
    line-height: 32px;
    color: var(--charcoal);
  }
  .services {
    list-style: none;
    margin: 12px 0 0;
    padding: 0;
    font-family: "Roboto", sans-serif;
    font-size: 24px;
    line-height: 30px;
  }
  .services li {
    position: relative;
    padding-left: 30px;
  }
  .services li::before {
    content: "";
    position: absolute;
    left: 4px;
    top: 12px;
    width: 7px;
    height: 7px;
    border-radius: 50%;
    background: var(--brand-red);
  }
  .contact {
    list-style: none;
    margin: 18px 0 0;
    padding: 0;
    font-family: "Roboto", sans-serif;
    font-size: 24px;
    line-height: 31px;
  }
  .contact li {
    display: flex;
    align-items: center;
    gap: 14px;
  }
  .contact svg {
    width: 18px;
    height: 18px;
    fill: var(--brand-red);
    flex: none;
  }
</style>
</head>
<body>
  <main class="business-card">
    <div class="brand-block">
      <span class="brand-block-square" aria-hidden="true"></span>
      <span class="brand-block-name">FLUE GUARDIAN</span>
    </div>

    <section class="details">
      <h1 class="company-name">FLUE GUARDIAN</h1>
      <p class="established">INC 1994</p>

      <p class="credentials">
        Serving Northern New England since 1994<br>
        Fully insured — Free estimates<br>
        Family owned &amp; operated
      </p>

      <ul class="services">
        <li>Full Masonry Services</li>
        <li>Historic chimney restoration</li>
        <li>Stainless steel liners</li>
        <li>New Chimney installations</li>
        <li>Fully Certified Chimney sweeps</li>
      </ul>

      <ul class="contact">
        <li>
          <svg viewBox="0 0 24 24" aria-hidden="true"><path d="M6.6 10.8a15.1 15.1 0 0 0 6.6 6.6l2.2-2.2c.3-.3.7-.4 1-.2 1.1.4 2.3.6 3.6.6.6 0 1 .4 1 1V20c0 .6-.4 1-1 1A17 17 0 0 1 3 4c0-.6.4-1 1-1h3.5c.6 0 1 .4 1 1 0 1.3.2 2.5.6 3.6.1.3 0 .7-.2 1z"/></svg>
          <span>802-555-0147</span>
        </li>
        <li>
          <svg viewBox="0 0 24 24" aria-hidden="true"><path d="M2 5h20v14H2z"/><path d="M2 6.5v-1.5h20v1.5l-10 7z" fill="var(--card)"/></svg>
          <span>info@flueguardianvt.example</span>
        </li>
        <li>
          <svg viewBox="0 0 24 24" aria-hidden="true"><circle cx="12" cy="12" r="10"/><path d="M7 8c2 0 3 1 3 3s-2 2-2 4M14 4c0 2 2 3 4 3M15 20c0-2 1-4 3-4" stroke="var(--card)" stroke-width="1.8" fill="none"/></svg>
          <span>www.flueguardianvt.example</span>
        </li>
      </ul>
    </section>
  </main>
</body>
</html>
```